Literary writer needs YOUR help for an e-book cover; must look good on Brindle pages

This short story is about an African-American college student who thrown in jail in Baltimore, the city that just had riots. Dorian is a Hollins Crest College, glasses-wearing college graduate, and on the night he is arrested, he is wearing a pink Hollins sweatshirt. He is taken in a white van to the police station and spends the weekend there. He doesn't quite believe this is happening to him because he has been insulated from the realities of race while he was a student.

The most important visual detail in the story is a $1 bill over which someone has taped triangles of the number 20 to make it look like a $20 bill. He was thrown in jail because a bar woman in a leopard skin bikini accused him of passing fake money. I did this cover myself on Canva, and I was thinking about a kind of noir feeling. The story is very depressing because Dorian is scared out of his mind. His weekend in jail changes his relationship with the two white friends who were out drinking with him. For anyone who has never been to Baltimore, the streets are very uneven and they are made of brick. I don't need a back cover or spine because this is just going to be an ebook. Thank you for your help!

Project Deadline Extended Reason: I don't want you to feel rushed, and I prefer to have the design be good, rather than have it be done sooner. Thank you for your help. Added Thursday, May 7, 2015

Target Market(s)

ebook buyers

Industry/Entity Type

College

Font styles to use
Serif
Sans Serif

Requirements
Must have
• Must look good at Brindle thumbnail size, and the title must be clearly readable
• Must also be sized correctly for the new Brindle ebook requirements.
• I should have stated the ebook dimensions. I'm looking for a design that is 1600 pixels wide and 2400 pixels tall. Thank you.
• The title Two Quiet Hours Past Midnight
• my name Rosalind Petrakis
Nice to have
• Maybe use the "fake" $20 bill that I describe above. It might make a good cover image. Maybe use an African-American man's fingers wrapped around jail bars.
• could also have the words a short story or A short story
Should not have
• If you use the hands, they can't have any jewelry on them.

```html
<!DOCTYPE html>
<html lang="en">
<head>
<meta charset="UTF-8">
<title>Two Quiet Hours Past Midnight — Cover</title>
<link href="https://fonts.googleapis.com/css2?family=Montserrat:wght@700;800&family=Oswald:wght@600&family=Open+Sans:wght@600;700&display=swap" rel="stylesheet">
<style>
  :root {
    --page-bg: #f1f1f1;
    --cover-ink: #0b0a0c;
    --street-teal: #1fb3c4;
    --street-amber: #c9762a;
    --street-red: #b8322a;
    --bill-light: #dfe3d2;
    --bill-mid: #a9b19a;
    --bill-shade: #5f6656;
    --frame-bronze: #8a6a44;
    --text-white: #ffffff;
    --title-yellow: #fbc10f;
  }
  * { margin: 0; padding: 0; box-sizing: border-box; }
  html, body {
    width: 1200px;
    height: 1200px;
    overflow: hidden;
    background: var(--page-bg);
  }
  .stage {
    position: relative;
    width: 1200px;
    height: 1200px;
  }
  .cover {
    position: absolute;
    left: 258px;
    top: 58px;
    width: 684px;
    height: 1082px;
    overflow: hidden;
    background: var(--cover-ink);
  }
  .street-backdrop {
    position: absolute;
    inset: 0;
    background:
      radial-gradient(ellipse 6% 3% at 20% 22%, rgba(184,50,42,0.7), transparent 100%),
      radial-gradient(ellipse 5% 3% at 55% 20%, rgba(184,50,42,0.6), transparent 100%),
      radial-gradient(ellipse 6% 3% at 82% 24%, rgba(184,50,42,0.55), transparent 100%),
      radial-gradient(ellipse 8% 4% at 40% 28%, rgba(240,240,240,0.35), transparent 100%),
      radial-gradient(ellipse 14% 4% at 60% 30%, rgba(31,179,196,0.55), transparent 100%),
      radial-gradient(ellipse 10% 6% at 14% 40%, rgba(184,50,42,0.65), transparent 100%),
      radial-gradient(ellipse 18% 42% at 70% 66%, rgba(31,179,196,0.6), transparent 100%),
      radial-gradient(ellipse 10% 34% at 8% 66%, rgba(201,118,42,0.6), transparent 100%),
      radial-gradient(ellipse 10% 34% at 94% 66%, rgba(201,118,42,0.5), transparent 100%),
      linear-gradient(180deg, #0c0b0e 0%, #16141a 22%, #2c1e18 32%, #3a2a20 40%, #1b2a2e 56%, #132026 76%, #0a0b0d 100%);
  }
  .glasses-area {
    position: absolute;
    left: 282px;
    top: 350px;
    width: 402px;
    height: 246px;
    border-radius: 50%;
    background: radial-gradient(ellipse 50% 50% at 55% 50%, rgba(138,106,68,0.45), rgba(31,179,196,0.15) 60%, transparent 100%);
  }
  .bill-area {
    position: absolute;
    left: 96px;
    top: 470px;
    width: 310px;
    height: 190px;
    border-radius: 10px;
    transform: rotate(-14deg);
    background: linear-gradient(135deg, var(--bill-light) 0%, var(--bill-mid) 55%, var(--bill-shade) 100%);
    box-shadow: 0 18px 40px rgba(0,0,0,0.55);
  }
  .author-name {
    position: absolute;
    top: 86px;
    left: 0;
    width: 100%;
    text-align: center;
    font-family: "Montserrat", sans-serif;
    font-weight: 800;
    font-size: 45px;
    word-spacing: 8px;
    color: var(--text-white);
  }
  .title {
    position: absolute;
    left: 34px;
    top: 742px;
    width: 640px;
  }
  .title-lead {
    display: block;
    font-family: "Open Sans", sans-serif;
    font-weight: 700;
    font-size: 44px;
    line-height: 1;
    color: var(--text-white);
    letter-spacing: -0.5px;
  }
  .title-main {
    display: block;
    margin-top: 14px;
    font-family: "Oswald", sans-serif;
    font-weight: 600;
    font-size: 138px;
    line-height: 1.04;
    color: var(--title-yellow);
    letter-spacing: -1px;
  }
  .subtitle {
    position: absolute;
    right: 36px;
    top: 958px;
    font-family: "Open Sans", sans-serif;
    font-weight: 600;
    font-size: 37px;
    letter-spacing: 2px;
    color: var(--text-white);
  }
</style>
</head>
<body>
  <main class="stage">
    <section class="cover">
      <div class="street-backdrop" role="img" aria-label="Wet city street at night with blurred red, teal and amber lights"></div>
      <div class="glasses-area" role="img" aria-label="Pair of cracked round wire-rimmed glasses lying on the wet pavement"></div>
      <div class="bill-area" role="img" aria-label="Folded one-dollar bill with taped-on twenty corners lying on the pavement"></div>
      <p class="author-name">Rosalind Petrakis</p>
      <h1 class="title">
        <span class="title-lead">Two Quiet Hours Past</span>
        <span class="title-main">Midnight</span>
      </h1>
      <p class="subtitle">a short story</p>
    </section>
  </main>
</body>
</html>
```